Dora Finch's Contemporary HOMEVEST Business Cards

I'd like a dark (almost black or black) background with some white lettering and some in a soft orange shade taken from the flowers. Print my photo large with all the lettering on the side opposite my photo. I'd like a simple, contemporary design similar to one I saw on your site. (All black with a tiny white line border inset from the edges. Glossy coating, please.

Target Market(s)

Real estate clients

Industry/Entity Type

Business

Contact Information for Business Card

medium weight cards

Font styles to use
Other font styles liked:
• Arial and perhaps Dora in script above printed name

Requirements
Must have
• Dora L. Finch
• CRS, GRI, ABR, SRES, e-PRO, CNE
• HOMEVEST Circle of Honor, Gold Key Agent
• HOMEVEST Career Excellence Award
• HOMEVEST Summit - Boulder
• 303 555-0142 . 303 555-0187 cell
• Dora@DoraFinchhomes.example
• ** Attached is the logo for the front of my business card. Please use the red one for HOMEVEST SUMMIT. Let me know if you need it in a different file type.
• On back of card please use this quote:
• “We have worked with Dora Finch on six real estate deals. Dora is prompt, efficient, always does what she says she’s going to do, and she keeps the process moving without being pushy. She’s unbelievably organized and never misses a detail. After having dealt with many hundreds of professional people in our lives, Dora stands out as one of the purely effective. Dora is one of those wonderful people who is not only kind and empathetic, but strong. She’s a great listener. We trust her as an advisor. Dora’s a smart lady who knows real estate—and this town—inside and out. Needless to say, we would work with Dora Finch again in an instant.
• ----- Carl Hudgens
Nice to have
• several creative ideas
• probably should remove dark circle sculpture in background if it shows
• maybe Dora in my script handwriting (orange)
Should not have
• don't know about this field

```html
<!DOCTYPE html>
<html lang="en">
<head>
<meta charset="utf-8">
<title>Dora L. Finch — Business Cards</title>
<link rel="stylesheet" href="https://fonts.googleapis.com/css2?family=Arimo:wght@400&family=Pinyon+Script&display=swap">
<style>
  :root {
    --backdrop: #8b6d49;
    --card-black: #000000;
    --text-white: #ffffff;
    --gold-light: #f6dcae;
    --gold-deep: #d9a155;
    --watermark: rgba(255, 255, 255, 0.06);
    --photo-dark: #141414;
    --photo-mid: #2a3a34;
    --photo-warm: #6b5444;
    --pattern-dark: #111111;
    --pattern-grey: #3a3a3a;
  }
  * { box-sizing: border-box; margin: 0; padding: 0; }
  html, body { width: 1000px; height: 1200px; overflow: hidden; }
  body { background: var(--backdrop); position: relative; font-family: "Arimo", Arial, sans-serif; }

  .card {
    position: absolute;
    left: 41px;
    width: 913px;
    height: 534px;
    background: var(--card-black);
    overflow: hidden;
    box-shadow: 0 6px 14px rgba(0, 0, 0, 0.55);
  }
  .card--front { top: 44px; }
  .card--back { top: 622px; width: 911px; }

  .front__monogram {
    position: absolute;
    left: 10px;
    top: -40px;
    font-family: "Pinyon Script", cursive;
    font-size: 460px;
    line-height: 1;
    color: var(--watermark);
    white-space: nowrap;
    pointer-events: none;
  }
  .front__name {
    position: absolute;
    left: 42px;
    top: 78px;
    font-family: "Pinyon Script", cursive;
    font-size: 62px;
    line-height: 1;
    background: linear-gradient(180deg, var(--gold-light) 20%, var(--gold-deep) 85%);
    -webkit-background-clip: text;
    background-clip: text;
    color: transparent;
  }
  .front__credentials {
    position: absolute;
    left: 44px;
    top: 196px;
    list-style: none;
    color: var(--text-white);
    font-size: 21.5px;
    line-height: 35px;
  }
  .front__contacts {
    position: absolute;
    left: 45px;
    top: 352px;
    list-style: none;
    color: var(--text-white);
    font-size: 24px;
    line-height: 39px;
  }
  .contact { display: flex; align-items: center; gap: 8px; }
  .contact__icon { width: 20px; height: 20px; flex: none; }

  .front__photo {
    position: absolute;
    right: 0;
    top: 0;
    width: 300px;
    height: 534px;
    background:
      radial-gradient(ellipse 70px 85px at 50% 18%, var(--photo-warm), transparent 100%),
      radial-gradient(ellipse 150px 230px at 55% 65%, var(--photo-mid), transparent 100%),
      var(--photo-dark);
  }

  .back__name {
    position: absolute;
    left: 70px;
    top: 222px;
    font-family: "Pinyon Script", cursive;
    font-size: 62px;
    line-height: 1;
    color: var(--text-white);
  }
  .back__pattern {
    position: absolute;
    right: 0;
    top: 0;
    width: 360px;
    height: 534px;
    background: linear-gradient(100deg, var(--card-black) 0%, var(--pattern-dark) 25%, var(--pattern-grey) 100%);
    opacity: 0.85;
  }
</style>
</head>
<body>

  <section class="card card--front" aria-label="Business card front">
    <div class="front__monogram" aria-hidden="true">Dor</div>
    <h1 class="front__name">Dora L. Finch</h1>
    <ul class="front__credentials">
      <li>CRS, GRI, ABR, SRES, e-PRO, CNE</li>
      <li>HOMEVEST Circle of Honor, Gold Key Agent</li>
      <li>HOMEVEST Career Excellence Award</li>
      <li>HOMEVEST Summit - Boulder</li>
    </ul>
    <ul class="front__contacts">
      <li class="contact">
        <svg class="contact__icon" viewBox="0 0 20 20" aria-hidden="true">
          <rect x="1" y="1" width="18" height="18" fill="#fff"/>
          <rect x="5" y="3" width="10" height="14" fill="#000"/>
          <rect x="6.5" y="4.5" width="7" height="3" fill="#fff"/>
          <g fill="#fff">
            <rect x="6.5" y="9" width="2" height="1.6"/><rect x="9" y="9" width="2" height="1.6"/><rect x="11.5" y="9" width="2" height="1.6"/>
            <rect x="6.5" y="11.5" width="2" height="1.6"/><rect x="9" y="11.5" width="2" height="1.6"/><rect x="11.5" y="11.5" width="2" height="1.6"/>
            <rect x="6.5" y="14" width="2" height="1.6"/><rect x="9" y="14" width="2" height="1.6"/><rect x="11.5" y="14" width="2" height="1.6"/>
          </g>
        </svg>
        <span>303 555-0142</span>
      </li>
      <li class="contact">
        <svg class="contact__icon" viewBox="0 0 20 20" aria-hidden="true">
          <rect x="1" y="1" width="18" height="18" fill="#fff"/>
          <path d="M4 8c0-2 2.5-3.5 6-3.5S16 6 16 8l-2.5 1-1-2h-5l-1 2z" fill="#000"/>
          <path d="M5.5 16l1.5-6h6l1.5 6z" fill="#000"/>
          <circle cx="10" cy="12.8" r="1.6" fill="#fff"/>
        </svg>
        <span>303 555-0187</span>
      </li>
      <li class="contact">
        <svg class="contact__icon" viewBox="0 0 20 20" aria-hidden="true">
          <rect x="1" y="1" width="18" height="18" fill="#fff"/>
          <rect x="3.5" y="5" width="13" height="10" fill="none" stroke="#000" stroke-width="1.6"/>
          <path d="M3.5 5l6.5 6 6.5-6M3.5 15l5-5M16.5 15l-5-5" fill="none" stroke="#000" stroke-width="1.4"/>
        </svg>
        <span>Dora@DoraFinchhomes.example</span>
      </li>
    </ul>
    <div class="front__photo" role="img" aria-label="Portrait photograph of Dora L. Finch seated, wearing a dark green top and a pearl necklace, against a black background"></div>
  </section>

  <section class="card card--back" aria-label="Business card back">
    <div class="back__pattern" role="img" aria-label="Grey floral and scroll ornament pattern along the right edge"></div>
    <p class="back__name">Dora L. Finch</p>
  </section>

</body>
</html>
```